Hi,

The project is a 2 page design of a deal aggregator website, the deals grid page, and the dedicated deal page , the wireframe layout can be found on http://www.pombrix.in. Some things to consider:

1. We will keep the animation as is, i.e. when the user clicks on any of the deal, the deal details shows up in the other page
2. we definitely need to set a color palette
3. The header will reman always on top
4. We're using a technique called infinite scroll, so the footer is never visible

It's an interesting project with a different take on the ui of the deals presentation.

Requirements
Nice to have
• i like the style of the following:
http://quillsy.com/shots/508217-Amber-Lanterns
http://quillsy.com/shots/736410-Brickmosse
http://quillsy.com/shots/640938-Harbor-Sketchbook

```html
<!DOCTYPE html>
<html lang="en">
<head>
<meta charset="utf-8">
<title>pombrix.in — deals</title>
<link rel="stylesheet" href="https://fonts.googleapis.com/css2?family=Ubuntu:wght@400;500;700&display=swap">
<style>
:root{
  --page:#f1f1f1;
  --band:#cfe77a;
  --band-edge:#b9cf66;
  --red:#e8351f;
  --price-red:#c8261a;
  --ink:#1b1b1b;
  --muted:#9a9a9a;
  --card:#ffffff;
  --card-line:#d6d6d6;
  --timer:#f1f1f1;
  --tick:#8cc63f;
}
*{margin:0;padding:0;box-sizing:border-box}
html,body{width:1200px;height:1200px;overflow:hidden}
body{background:var(--page);font-family:"Ubuntu",sans-serif;color:var(--ink);position:relative}
.site-header{position:absolute;left:0;top:20px;width:1200px;height:87px;background:var(--band);border-top:3px solid #a8a8a8;border-bottom:2px solid var(--band-edge)}
.brand{position:absolute;left:140px;top:24px;display:flex;align-items:center;gap:8px;font-weight:700;font-size:32px;letter-spacing:-1.5px;color:var(--ink)}
.brand-mark{width:16px;height:16px;background:var(--red)}
.main-nav{position:absolute;left:348px;top:27px;display:flex;gap:0;font-weight:500;font-size:16px}
.main-nav a{color:var(--ink);text-decoration:none;padding:8px 12px;letter-spacing:.3px}
.main-nav a.active{background:#eef5cf;border:1px solid #dfe9b4;font-weight:700}
.deal-count{position:absolute;left:790px;top:-5px;width:200px;height:92px}
.deal-count .shadow{position:absolute;inset:0;background:#8c8c8c;transform:skewX(-4deg) translateX(-4px)}
.deal-count .face{position:absolute;inset:0;background:var(--red);transform:skewX(-3deg);color:#fff;text-align:center}
.deal-count .num{display:block;font-weight:500;font-size:52px;line-height:1;padding-top:18px;letter-spacing:1px}
.deal-count .lbl{display:block;font-weight:500;font-size:16px;color:#1b1b1b;margin-top:-2px}
.sort{position:absolute;left:133px;top:131px}
.label{font-size:13px;font-weight:500;color:var(--ink)}
.sort .label{margin-left:10px}
.sort-tabs{margin-top:4px;width:397px;height:36px;background:linear-gradient(90deg,#fff,#fafafa 70%,rgba(255,255,255,0));display:flex;align-items:center;gap:13px;padding-left:12px;font-size:17px;color:var(--muted)}
.sort-tabs .on{color:var(--ink)}
.categories{position:absolute;left:554px;top:131px;width:510px}
.cat-list{margin-top:6px;font-size:15px;line-height:20px;color:var(--muted)}
.cat-list .on{color:var(--ink)}
.deal{position:absolute;width:300px}
.deal-box{height:178px;background:var(--card);border:1px solid var(--card-line);position:relative}
.deal-photo{position:absolute;left:13px;top:13px;width:219px;height:151px}
.timer{position:absolute;left:246px;top:6px;width:47px;height:164px;background:var(--timer);padding:45px 0 0 10px;font-size:13px;line-height:14px}
.timer b{display:block;color:var(--price-red);font-size:17px;line-height:17px}
.timer span{display:block;margin-bottom:12px}
.price{position:relative;height:30px}
.price .d{position:absolute;left:14px;top:3px;font-size:10px}
.price .pct{position:absolute;left:14px;top:14px;font-weight:700;font-size:16px;color:var(--price-red)}
.price .was{position:absolute;left:72px;top:14px;font-weight:700;font-size:15px;color:var(--price-red);text-decoration:line-through}
.price .now{position:absolute;left:143px;top:12px;font-weight:500;font-size:18px;color:var(--price-red)}
.price svg{position:absolute;left:190px;top:5px}
</style>
</head>
<body>
<header class="site-header">
  <div class="brand"><span>pombrix.in</span><span class="brand-mark"></span></div>
  <nav class="main-nav"><a class="active" href="#">HOME</a><a href="#">WIDGET</a><a href="#">DELTA DESKS</a></nav>
  <div class="deal-count"><div class="shadow"></div><div class="face"><span class="num">1897</span><span class="lbl">DEALS FOUND</span></div></div>
</header>

<section class="sort">
  <div class="label">sort by</div>
  <div class="sort-tabs"><span class="on">Discount</span><span>Popular</span><span>New</span><span>Saving</span><span>Timeleft</span></div>
</section>
<section class="categories">
  <div class="label">categories</div>
  <div class="cat-list"><span class="on">Electronics</span>, Clothing Shoes and Jewellery, Home and Office, Health and Beauty, Entertainment and Activities, Travel</div>
</section>

<main>
<article class="deal" style="left:133px;top:212px"><div class="deal-box"><div class="deal-photo" role="img" aria-label="Air purifier product shot" style="background:linear-gradient(90deg,#fff,#cfdbe6 50%,#fff)"></div><div class="timer"><b>6</b><span>Days</span><b>11</b><span>hours</span><b>21</b><span>mins</span></div></div><div class="price"><span class="d">discount</span><span class="pct">50%</span><span class="was">110 LE</span><span class="now">55 LE</span><svg width="24" height="22" viewBox="0 0 24 22"><path d="M2 12l7 7L22 2" fill="none" stroke="#8cc63f" stroke-width="4"/></svg></div></article>
<article class="deal" style="left:446px;top:212px"><div class="deal-box"><div class="deal-photo" style="left:10px;top:13px;width:224px" role="img" aria-label="Relaxing spa massage" style="" ></div><div class="timer"><b>6</b><span>Days</span><b>11</b><span>hours</span><b>21</b><span>mins</span></div></div><div class="price"><span class="d">discount</span><span class="pct">50%</span><span class="was">110 LE</span><span class="now">55 LE</span><svg width="24" height="22" viewBox="0 0 24 22"><path d="M2 12l7 7L22 2" fill="none" stroke="#8cc63f" stroke-width="4"/></svg></div></article>
<article class="deal" style="left:758px;top:212px"><div class="deal-box"><div class="deal-photo" role="img" aria-label="Portable speaker on orange backdrop" style="left:16px;background:linear-gradient(90deg,#2a2a2a,#555 35%,#f4b41a 60%,#f59a08)"></div><div class="timer"><b>6</b><span>Days</span><b>11</b><span>hours</span><b>21</b><span>mins</span></div></div><div class="price"><span class="d">discount</span><span class="pct">50%</span><span class="was">110 LE</span><span class="now">55 LE</span><svg width="24" height="22" viewBox="0 0 24 22"><path d="M2 12l7 7L22 2" fill="none" stroke="#8cc63f" stroke-width="4"/></svg></div></article>

<article class="deal" style="left:133px;top:478px"><div class="deal-box"><div class="deal-photo" role="img" aria-label="Cordless phone handset" style="background:linear-gradient(90deg,#e6e6e6,#c9c9c9 70%,#333 80%,#ddd)"></div><div class="timer"><b>6</b><span>Days</span><b>11</b><span>hours</span><b>21</b><span>mins</span></div></div><div class="price"><span class="d">discount</span><span class="pct">50%</span><span class="was">110 LE</span><span class="now">55 LE</span><svg width="24" height="22" viewBox="0 0 24 22"><path d="M2 12l7 7L22 2" fill="none" stroke="#8cc63f" stroke-width="4"/></svg></div></article>
<article class="deal" style="left:446px;top:478px"><div class="deal-box"><div class="deal-photo" role="img" aria-label="Assorted eyeglass frames" style="left:11px;width:223px;background:linear-gradient(135deg,#f4f4f4,#d8d8d8)"></div><div class="timer"><b>6</b><span>Days</span><b>11</b><span>hours</span><b>21</b><span>mins</span></div></div><div class="price"><span class="d">discount</span><span class="pct">50%</span><span class="was">110 LE</span><span class="now">55 LE</span><svg width="24" height="22" viewBox="0 0 24 22"><path d="M2 12l7 7L22 2" fill="none" stroke="#8cc63f" stroke-width="4"/></svg></div></article>
<article class="deal" style="left:758px;top:478px"><div class="deal-box"><div class="deal-photo" role="img" aria-label="Fitness couple in the gym" style="left:13px;background:linear-gradient(135deg,#8a8580,#6f6a64 50%,#a8a39c)"></div><div class="timer"><b>6</b><span>Days</span><b>11</b><span>hours</span><b>21</b><span>mins</span></div></div><div class="price"><span class="d">discount</span><span class="pct">50%</span><span class="was">110 LE</span><span class="now">55 LE</span><svg width="24" height="22" viewBox="0 0 24 22"><path d="M2 12l7 7L22 2" fill="none" stroke="#8cc63f" stroke-width="4"/></svg></div></article>

<article class="deal" style="left:133px;top:734px"><div class="deal-box"><div class="deal-photo" role="img" aria-label="Wax strip packs" style="background:linear-gradient(90deg,#c7e0a0,#f0b5c8 45%,#f6c79a)"></div><div class="timer"><b>6</b><span>Days</span><b>11</b><span>hours</span><b>21</b><span>mins</span></div></div><div class="price"><span class="d">discount</span><span class="pct">50%</span><span class="was">110 LE</span><span class="now">55 LE</span><svg width="24" height="22" viewBox="0 0 24 22"><path d="M2 12l7 7L22 2" fill="none" stroke="#8cc63f" stroke-width="4"/></svg></div></article>
<article class="deal" style="left:446px;top:734px"><div class="deal-box"><div class="deal-photo" role="img" aria-label="Colour festival event poster" style="left:12px;width:222px;background:radial-gradient(circle at 45% 55%,#8a3a10,#e8531f 35%,#f6c02a 55%,#fff 80%)"></div><div class="timer"><b>6</b><span>Days</span><b>11</b><span>hours</span><b>21</b><span>mins</span></div></div><div class="price"><span class="d">discount</span><span class="pct">50%</span><span class="was">110 LE</span><span class="now">55 LE</span><svg width="24" height="22" viewBox="0 0 24 22"><path d="M2 12l7 7L22 2" fill="none" stroke="#8cc63f" stroke-width="4"/></svg></div></article>
<article class="deal" style="left:758px;top:734px"><div class="deal-box"><div class="deal-photo" role="img" aria-label="Row of backpacks" style="left:13px;background:linear-gradient(180deg,#2d2d2d,#5a5a5a 50%,#1f1f1f)"></div><div class="timer"><b>6</b><span>Days</span><b>11</b><span>hours</span><b>21</b><span>mins</span></div></div><div class="price"><span class="d">discount</span><span class="pct">50%</span><span class="was">110 LE</span><span class="now">55 LE</span><svg width="24" height="22" viewBox="0 0 24 22"><path d="M2 12l7 7L22 2" fill="none" stroke="#8cc63f" stroke-width="4"/></svg></div></article>

<article class="deal" style="left:133px;top:1000px"><div class="deal-box"><div class="deal-photo" role="img" aria-label="Tropical resort with pool and beach" style="left:16px;top:10px;width:216px;background:linear-gradient(180deg,#3b77b8,#7fb0d8 35%,#2e8a6a 65%,#23b0c8)"></div><div class="timer"><b>6</b><span>Days</span><b>11</b><span>hours</span><b>21</b><span>mins</span></div></div><div class="price"><span class="d">discount</span></div></article>
<article class="deal" style="left:446px;top:1000px"><div class="deal-box"><div class="deal-photo" role="img" aria-label="Plated rice and grilled dish" style="left:14px;top:10px;width:220px;background:radial-gradient(circle at 50% 55%,#e8d9b0,#b89660 40%,#2a2a2a 75%)"></div><div class="timer"><b>6</b><span>Days</span><b>11</b><span>hours</span><b>21</b><span>mins</span></div></div><div class="price"><span class="d">discount</span></div></article>
<article class="deal" style="left:758px;top:1000px"><div class="deal-box"><div class="deal-photo" role="img" aria-label="Skincare beauty portrait" style="left:13px;top:10px;background:linear-gradient(90deg,#b9a699,#e6d3c6 50%,#fff)"></div><div class="timer"><b>6</b><span>Days</span><b>11</b><span>hours</span><b>21</b><span>mins</span></div></div><div class="price"><span class="d">discount</span></div></article>
</main>
<style>.deal:nth-of-type(2) .deal-photo{background:linear-gradient(90deg,#e9c9b4,#f3ddd0 50%,#2b2b2b)}</style>
</body>
</html>
```